Professional Hairdresser needs powerful, clever, simple, modern business card

I need a professional, clever, powerful, bold, attractive, modern/simplistic business card.
I specialize in dimensional hair color, precision haircutting, modern classic design, and signature finishes.
I believe in advanced education, continued training with emphasis on perfect practice, and strive to be the best at what I do.
I am trained by the industry's best and have passion for what I do, I want my business card to reflect my talents, education, capabilities, signature color techniques and design and confidence.
I want to be known as reputable, bold, artistic, aware, classic yet modern, innovative, creative, dimensional, knowledgeable, and educated.
I want something bold, simple, elegant, modern, clever, and legible.
My personal style is progressive, modern, eclectic, clean with modern luxury comfort style.
I love the use of black and white, to creative visual interest and texture. I think putting black as a solid background with white bold font makes the words jump/glow to the eye. I also think a stark white background with bold black fonts looks great, maybe with a punch of red. It is simple, clean, elegant.
I have a QR code I would like to include on the card but have no idea how to make it visually pleasing or make sense.
I do not have a set logo and am not sure if this needs to be done first or if the business card should be done first.

Target Market(s)

Early 20's-mid 60's, female and male, fashion aware, people who can afford my prices, appreciate value

Industry/Entity Type

Training

Requirements
Must have
• I would like to incorporate the QR code I have if possible.
I would like to have my name and contact info.
I would like my logo (or maybe have my logo be RT in a font like listed below).
I would like the fonts to be modern, bold, clean, readable.
Fonts I have looked at are: The font used on the book called: Vexaro A Hundred Years of Hue" I really love. I have looked at glyphvault.example for font and found "Georgiquas", but the designer wanted 200 euros which I just dont have at the time. Others I looked at include "Lin Libertine", Alien-Encounters-solid-regular-italic".
I love font used in the picture I included with the Tobin.Ashcroft ad.
Clean, modern, professional, legible, structured.
Nice to have
• I envision a black background with bold, modern, simple, font in white creating the effect of the words jumping off the card, visually apparent and glowing. Like a really expensive restaurant with a sign that you cant miss because the name is in bright white on black background, simple, bold, modern but not futuristic, powerful, clever, elegant, and draws the eye making it unforgetable. Perhaps layering black and white in order to where the font will be in white.
I see balance and chic.
Perhaps
Should not have
• I appreciate the trends in business design, but realize trends come and go and not sure if having something "trendy" is advisable for me. Having said that, I like creative modern design and sometimes current trends are important in design. I do like red as accent color, the primary blue color, blue on the PixelForum page, the masculine/florescent purple, and the neo bold yellow and the primary color shade of yellow.
I do not want clutter.
I do not want any fonts that are swirly, old-world calligraphy, script, or penmanship style.
I do not want picture of scissors, heads of old-school beauty school hair, or barber poles.

```html
<!DOCTYPE html>
<html lang="en">
<head>
<meta charset="utf-8">
<title>Rowan Tate Professional Hair — Business Card</title>
<link rel="stylesheet" href="https://fonts.googleapis.com/css2?family=Michroma&family=Quicksand:wght@500&display=swap">
<style>
  :root {
    --page-bg: #2b2b2b;
    --card-black: #050505;
    --card-glow: #2a2d30;
    --ink-white: #ffffff;
    --ink-soft: #e6e6e6;
    --rule: rgba(255,255,255,0.16);
  }
  * { margin: 0; padding: 0; box-sizing: border-box; }
  html, body {
    width: 1200px; height: 1000px; overflow: hidden;
    background: var(--page-bg);
  }
  .canvas { position: relative; width: 1200px; height: 1000px; }
  .card {
    position: absolute; left: 222px; width: 736px; height: 402px;
    background:
      radial-gradient(ellipse 360px 300px at 400px 190px, var(--card-glow) 0%, rgba(20,22,24,0.6) 45%, transparent 80%),
      var(--card-black);
    box-shadow: 0 6px 18px rgba(0,0,0,0.55);
    overflow: hidden;
  }
  .card--front { top: 88px; }
  .card--back { top: 528px; }
  .divider {
    position: absolute; left: 398px; width: 1px;
    background: linear-gradient(to bottom, transparent, var(--rule) 30%, var(--rule) 70%, transparent);
  }
  .card--front .divider { top: 110px; height: 200px; }
  .card--back .divider { top: 95px; height: 210px; }

  .wordmark {
    position: absolute; right: 361px; top: 172px; text-align: right;
    color: var(--ink-white);
  }
  .wordmark__name {
    font-family: "Michroma", sans-serif;
    font-size: 27px; line-height: 1; letter-spacing: -1px;
    display: block;
  }
  .wordmark__trade {
    font-family: "Michroma", sans-serif;
    font-size: 9.5px; letter-spacing: 0.5px; line-height: 1;
    display: block; margin-top: 3px; margin-right: 2px;
  }
  .monogram {
    position: absolute; left: 424px; top: 124px;
    font-family: "Michroma", sans-serif;
    font-size: 100px; line-height: 1; letter-spacing: -4px;
    color: var(--ink-white);
  }

  .contact {
    position: absolute; right: 130px; top: 146px;
    list-style: none;
    font-family: "Quicksand", sans-serif; font-weight: 500;
    font-size: 14px; color: var(--ink-soft);
  }
  .contact__item {
    display: flex; align-items: center; justify-content: flex-end;
    height: 30.5px;
  }
  .contact__icon {
    width: 22px; height: 18px; margin-left: 30px; margin-right: -64px; flex: none;
  }
</style>
</head>
<body>
<main class="canvas">
  <section class="card card--front" aria-label="Card front">
    <div class="wordmark">
      <span class="wordmark__name">ROWAN TATE</span>
      <span class="wordmark__trade">PROFESSIONAL HAIR</span>
    </div>
    <div class="divider"></div>
    <div class="monogram">RT</div>
  </section>

  <section class="card card--back" aria-label="Card back">
    <ul class="contact">
      <li class="contact__item">555 204 781
        <svg class="contact__icon" viewBox="0 0 22 18" aria-hidden="true">
          <path d="M2 6 Q11 0 20 6 L18 8 L15 7 L15 5 Q11 3.5 7 5 L7 7 L4 8 Z" fill="#fff"/>
          <rect x="5" y="9" width="12" height="8" rx="1.5" fill="#fff"/>
          <circle cx="11" cy="13" r="2" fill="#050505"/>
        </svg>
      </li>
      <li class="contact__item">4120 Harbor Lane Marlow Bay, CA 90412
        <svg class="contact__icon" viewBox="0 0 22 18" aria-hidden="true">
          <path d="M11 1 C7.5 1 5.5 3.5 5.5 6.3 C5.5 10 11 17 11 17 C11 17 16.5 10 16.5 6.3 C16.5 3.5 14.5 1 11 1 Z" fill="#fff"/>
          <circle cx="11" cy="6.3" r="2.2" fill="#050505"/>
        </svg>
      </li>
      <li class="contact__item">hello@rowantate.example
        <svg class="contact__icon" viewBox="0 0 22 18" aria-hidden="true">
          <rect x="1" y="3" width="20" height="12" fill="#fff"/>
          <path d="M1 3 L11 10 L21 3" fill="none" stroke="#050505" stroke-width="1.3"/>
        </svg>
      </li>
      <li class="contact__item">Chirpline.example/RowanTate
        <svg class="contact__icon" viewBox="0 0 22 18" aria-hidden="true">
          <circle cx="11" cy="9" r="7" fill="#fff"/>
        </svg>
      </li>
    </ul>
    <div class="divider"></div>
  </section>
</main>
</body>
</html>
```